Inspiring Poster for Company Staff Room

What we need:
We want an awesome design to create a poster that will be plaque mounted in our staff room. We just went through a very motivating workshop to discover our "WHY" as a company...basically, to define the reason we are in business, and to define what motivates us to come to work every day. The poster must be motivating but really resonate with our team…we are not looking for a “typical” motivational poster that we can purchase off Zentrix!

Who we are:
We are a property management company, a team of 20 that is passionate about our investors, and residents who rent from us, but more importantly, we love helping people and making a difference in our industry. We are proud and work hard for every single 5 star Valoro review we achieve.

Information for you:
We have included a mock up of the poster, which words we want, and the placement of them (in a general sense) but we need a designer to really bring this together in an inspiring poster that represents our company’s culture, feel, and fit. We have also included a logo file, as well as examples of our business cards, letterhead and thank you card already designed.
Here are the parameters:

(1) Poster size: 24” x 36”
(2) Full colour
(3) Must incorporate our company logo
(4) Must incorporate the following words:

Why do I come to work?

“To feel fulfilled by empathizing, educating and empowering our clients and co-workers so that we can build strong, impactful relationships”

Own the outcome

(5) Please see our website at www.brindlecovepm.example to get a feel for our company culture and for a better idea of our current company graphics

Target Market(s)

Our staff. Will not be seen by our clients

Industry/Entity Type

Real Estate

Font styles to use
Serif
Sans Serif

Requirements
Should not have
• Would not want this to be too "busy." if you can picture it, the poster will be mounted on the wall as soon as someone enters the room. The idea is to remind them each day why they come to work.

```html
<!DOCTYPE html>
<html lang="en">
<head>
<meta charset="utf-8">
<title>Why Do I Come to Work? – Staff Room Poster</title>
<link rel="stylesheet" href="https://fonts.googleapis.com/css2?family=Archivo+Black&family=Karla:wght@400&family=Playfair+Display:wght@700&display=swap">
<style>
  :root {
    --paper: #ffffff;
    --ink: #0a0c0e;
    --quote-cyan: #94ffff;
    --brand-blue: #2fb0f2;
    --brand-dark: #2c3236;
  }
  * { margin: 0; padding: 0; box-sizing: border-box; }
  html, body {
    width: 1200px;
    height: 800px;
    overflow: hidden;
    background: var(--paper);
  }
  .poster {
    position: relative;
    width: 1200px;
    height: 800px;
    background: var(--paper);
    color: var(--ink);
  }
  .quote-mark {
    position: absolute;
    left: 250px;
    top: 58px;
    font-family: "Playfair Display", Georgia, serif;
    font-weight: 700;
    font-size: 330px;
    line-height: 1;
    color: var(--quote-cyan);
  }
  .headline {
    position: absolute;
    left: 300px;
    top: 168px;
    width: 610px;
    text-align: center;
    font-family: "Archivo Black", "Arial Black", sans-serif;
    font-size: 64px;
    line-height: 53px;
    letter-spacing: -1px;
    text-transform: uppercase;
  }
  .headline span { display: block; }
  .mission {
    position: absolute;
    left: 330px;
    top: 329px;
    width: 550px;
    text-align: center;
    font-family: "Karla", "Helvetica Neue", sans-serif;
    font-weight: 400;
    font-size: 30px;
    line-height: 35px;
    letter-spacing: 0.5px;
  }
  .mission span { display: block; }
  .motto {
    position: absolute;
    left: 300px;
    top: 561px;
    width: 610px;
    text-align: center;
    font-family: "Archivo Black", "Arial Black", sans-serif;
    font-size: 54px;
    line-height: 60px;
    letter-spacing: -1px;
    text-transform: uppercase;
  }
  .company-mark {
    position: absolute;
    left: 974px;
    top: 752px;
    display: flex;
    align-items: center;
    gap: 8px;
  }
  .company-mark__square {
    width: 32px;
    height: 32px;
    background: var(--brand-dark);
  }
  .company-mark__name {
    font-family: "Archivo Black", "Arial Black", sans-serif;
    font-size: 12px;
    line-height: 14px;
    letter-spacing: 1px;
    color: var(--brand-blue);
    text-transform: uppercase;
  }
  .company-mark__name span { display: block; }
</style>
</head>
<body>
  <main class="poster">
    <div class="quote-mark" aria-hidden="true">&ldquo;</div>

    <h1 class="headline">
      <span>Why do I come</span>
      <span>to work?</span>
    </h1>

    <p class="mission">
      <span>&ldquo;To feel fulfilled by empathizing,</span>
      <span>educating and empowering</span>
      <span>our clients and co-workers</span>
      <span>so that we can build strong,</span>
      <span>impactful relationships.&rdquo;</span>
    </p>

    <p class="motto">Own the outcome.</p>

    <div class="company-mark">
      <div class="company-mark__square" aria-hidden="true"></div>
      <p class="company-mark__name">
        <span>Brindle Cove</span>
        <span>Property Management</span>
      </p>
    </div>
  </main>
</body>
</html>
```